IT Product Event Invitations

We are requesting the design of two invitations for a series of technological events that will be held between the company Tidewell Core and its partner in the Dominican Republic, Velorbit.
Both events represent the launch of the Tidewell Core brand in the Dominican Republic.
The first event is an elegant dinner aimed at the banking sector of the Dominican Republic to showcase the "Ledgerline Banking Suite" software.
Event information:
- Descriptive text for the invitation: Velorbit y Tidewell Core le invitan a descubrir cómo reducir costos, aumentar la automatización y mejorar la satisfacción de los clientes a través de una solución única para enfrentar los desafíos de la banca.
- Date: 25 de Septiembre
- Time: 7PM
- Location: El Mirtal, Av. Julio Benavente 318
In the invitation, consider using the colors of the Tidewell Core and Velorbit brands if possible. You can find the logos in the webpage
The second event is a wine tasting to present "Crestway Operations Hub" aimed at various industries.
Event information:
- Descriptive text for the invitation: Velorbit y Tidewell Core le invitan a conocer una solución que le permitirá a toda su empresa brindar una experiencia de servicio a otro nivel.
- Date: 26 de Septiembre
- Time: 7PM
In the invitation, consider using the colors of the Tidewell Core and Velorbit brands if possible. You can find the logos in the web page.
Both invitations must have a button for participant registration and that when you click on the image, it will direct you to a form.
Form for Ledgerline Banking Suite: https://signup.palvento-forms.example/event/k3rq9-banking-dinner-7xw2
Form for Crestway Operations Hub: https://signup.palvento-forms.example/event/m8vt4-wine-tasting-2jq5
Target Market(s)
Enterprise Customers
Industry/Entity Type
Technology
Look and feel
Each slider illustrates characteristics of the customer's brand and the style your logo design should communicate.

```html
<!DOCTYPE html>
<html lang="es">
<head>
<meta charset="utf-8">
<title>Invitación – Ledgerline Banking Suite</title>
<link rel="stylesheet" href="https://fonts.googleapis.com/css2?family=Didact+Gothic&family=Outfit:wght@500;600;700&display=swap">
<style>
  :root {
    --page-bg: #efeeee;
    --tan-dark: #c8aa8d;
    --cream-a: #e9dccd;
    --cream-b: #f4eee2;
    --ink: #2b2724;
    --ink-soft: #3d3733;
    --rule: #4a423c;
    --accent-red: #d42a2f;
    --go-green: #7ddb69;
    --go-green-edge: #6bd658;
    --white: #ffffff;
  }
  * { margin: 0; padding: 0; box-sizing: border-box; }
  html, body {
    width: 1200px; height: 762px; overflow: hidden;
    background: var(--page-bg);
  }
  .invite {
    position: absolute; left: 0; top: 63px;
    width: 1200px; height: 635px;
    background: linear-gradient(100deg, var(--cream-a) 0%, var(--cream-b) 100%);
    overflow: hidden;
    font-family: "Didact Gothic", "Century Gothic", sans-serif;
    color: var(--ink);
    text-decoration: none;
    display: block;
  }
  .invite__bands { position: absolute; inset: 0; }
  .brand-bar {
    position: absolute; top: 56px; left: 0; width: 1200px; height: 69px;
  }
  .brand-name {
    position: absolute; top: 14px;
    font-family: "Outfit", sans-serif; font-weight: 700;
    font-size: 34px; line-height: 40px; color: var(--ink);
    letter-spacing: -0.5px;
  }
  .brand-name--host { left: 96px; }
  .brand-name--partner { left: 432px; display: flex; align-items: center; gap: 10px; }
  .brand-dot {
    width: 26px; height: 26px; border-radius: 50%;
    background: var(--accent-red);
  }
  .brand-divider {
    position: absolute; left: 372px; top: 0; width: 2px; height: 69px;
    background: var(--ink);
  }
  .headline {
    position: absolute; left: 148px; width: 400px; top: 180px;
    text-align: center;
    font-family: "Outfit", sans-serif; font-weight: 500;
    font-size: 54px; line-height: 64px; color: var(--ink);
  }
  .intro {
    position: absolute; left: 58px; width: 580px; top: 243px;
    text-align: center; font-size: 19.5px; line-height: 24.5px;
    color: var(--ink-soft);
  }
  .schedule {
    position: absolute; left: 226px; top: 381px; width: 246px; height: 122px;
  }
  .schedule svg { position: absolute; inset: 0; }
  .schedule__date {
    position: absolute; left: 0; right: 0; top: 47px; text-align: center;
    font-family: "Outfit", sans-serif; font-weight: 600; font-size: 23px;
    color: var(--ink);
  }
  .schedule__time {
    position: absolute; left: 0; right: 0; top: 86px; text-align: center;
    font-family: "Outfit", sans-serif; font-weight: 600; font-size: 23px;
    color: var(--ink);
  }
  .venue {
    position: absolute; left: 118px; top: 554px;
    display: flex; align-items: center; gap: 14px;
    font-size: 23px; color: var(--ink-soft);
  }
  .table-photo {
    position: absolute; left: 680px; top: 66px; width: 468px; height: 468px;
    border-radius: 50%;
    background: radial-gradient(circle at 50% 48%, #f6f3ee 0%, #eeebe6 55%, #e6e1da 80%, #efe7dc 100%);
    box-shadow: 0 6px 24px rgba(140, 110, 80, 0.18);
  }
  .register {
    position: absolute; left: 668px; top: 495px; width: 474px; height: 95px;
    border: 2px solid var(--go-green-edge); border-radius: 26px;
    padding: 5px;
  }
  .register__fill {
    width: 100%; height: 100%; border-radius: 20px;
    background: var(--go-green);
    display: flex; flex-direction: column; align-items: center; justify-content: center;
    color: var(--white);
  }
  .register__main {
    font-family: "Outfit", sans-serif; font-weight: 700;
    font-size: 41px; line-height: 38px; letter-spacing: 0.5px;
  }
  .register__sub {
    font-family: "Outfit", sans-serif; font-weight: 500;
    font-size: 16px; letter-spacing: 5px; line-height: 20px; margin-top: 2px;
  }
</style>
</head>
<body>
<a class="invite" href="https://signup.palvento-forms.example/event/k3rq9-banking-dinner-7xw2" aria-label="Invitación a la cena Ledgerline Banking Suite – registrarse">
  <svg class="invite__bands" width="1200" height="635" viewBox="0 0 1200 635" aria-hidden="true">
    <polygon points="0,0 92,0 431,635 0,635" fill="var(--tan-dark)"/>
    <polygon points="1040,0 1200,0 1200,240" fill="var(--tan-dark)"/>
  </svg>

  <div class="brand-bar">
    <span class="brand-name brand-name--host">Tidewell Core</span>
    <span class="brand-divider"></span>
    <span class="brand-name brand-name--partner"><span class="brand-dot"></span>Velorbit</span>
  </div>

  <h1 class="headline">Invitación</h1>
  <p class="intro">Velorbit y Tidewell Core le invitan a descubrir cómo reducir costos, aumentar la automatización y mejorar la satisfacción de los clientes a través de una solución única para enfrentar los desafíos de la banca.</p>

  <div class="schedule">
    <svg width="246" height="122" viewBox="0 0 246 122" aria-hidden="true">
      <path d="M0.5 122 V24.5 H88" fill="none" stroke="var(--rule)" stroke-width="1"/>
      <path d="M158 24.5 H245.5 V122" fill="none" stroke="var(--rule)" stroke-width="1"/>
      <line x1="20" y1="81.5" x2="226" y2="81.5" stroke="var(--rule)" stroke-width="1.5"/>
      <g transform="translate(99,3)">
        <rect x="1.5" y="5" width="45" height="36" rx="3" fill="none" stroke="var(--ink)" stroke-width="2.5"/>
        <rect x="1.5" y="5" width="45" height="7" fill="var(--accent-red)"/>
        <line x1="10" y1="1" x2="10" y2="8" stroke="var(--ink)" stroke-width="2.5"/>
        <line x1="20" y1="1" x2="20" y2="8" stroke="var(--ink)" stroke-width="2.5"/>
        <line x1="30" y1="1" x2="30" y2="8" stroke="var(--ink)" stroke-width="2.5"/>
        <line x1="40" y1="1" x2="40" y2="8" stroke="var(--ink)" stroke-width="2.5"/>
        <line x1="7" y1="21" x2="14" y2="21" stroke="var(--ink)" stroke-width="2.5"/>
        <line x1="7" y1="28" x2="14" y2="28" stroke="var(--ink)" stroke-width="2.5"/>
        <line x1="7" y1="35" x2="14" y2="35" stroke="var(--ink)" stroke-width="2.5"/>
        <circle cx="34" cy="32" r="12" fill="var(--go-green)" stroke="var(--ink)" stroke-width="2.5"/>
        <path d="M34 25 V32 H39" fill="none" stroke="var(--ink)" stroke-width="2.2"/>
      </g>
    </svg>
    <div class="schedule__date">25 de Septiembre</div>
    <div class="schedule__time">7:00PM</div>
  </div>

  <div class="venue">
    <svg width="30" height="34" viewBox="0 0 30 34" aria-hidden="true">
      <path d="M15 27 C15 27 5 17 5 11 A10 10 0 0 1 25 11 C25 17 15 27 15 27 Z" fill="none" stroke="var(--accent-red)" stroke-width="2"/>
      <circle cx="15" cy="11" r="4" fill="none" stroke="var(--accent-red)" stroke-width="2"/>
      <ellipse cx="15" cy="29" rx="12" ry="3.5" fill="none" stroke="var(--accent-red)" stroke-width="2"/>
    </svg>
    <span>El Mirtal, Av. Julio Benavente 318</span>
  </div>

  <div class="table-photo" role="img" aria-label="Fotografía de un plato blanco con cuchara, cuchillo y tenedor color cobre atados con cordel y una etiqueta"></div>

  <div class="register">
    <div class="register__fill">
      <span class="register__main">CLICK HERE</span>
      <span class="register__sub">TO REGISTER</span>
    </div>
  </div>
</a>
</body>
</html>
```